Chai Tea Company needs a Tea Packaging Box Design

Tea Packaging
Dimensions of the Tea Packaging Box: Height 13 cm; Width 8.5 cm; Depth 7 cm
Individual Teabag Packet/ Sachet: Width 6.5 cm; Length 8.25 cm
We are looking for a new tea packaging design, for our tea business. The material of the box is cardboard. We are also looking for a design that will be on each individual tea bag sachet/packet that goes into the box. This design will be very similar to what you design for the tea packaging box.
Product Info:
Our tea company is called “Velmora Leaf”. We sell two types of Chai Tea, once called “Velmora Gold” and one called “Velmora Bloom”. The Velmora Gold has caffeine, while the Velmora Bloom is Naturally Caffeine Free. The Velmora Gold has a black tea base, while the Velmora Bloom has a Rooibos tea base. We will need two tea packaging designs, one for each Chai Tea flavour. The designs for both the teas can be similar, but make sure that you can easily distinguish one from the other (example: make them have different colours or pictures). Both the chai teas, come from the same product line.
Tea Packaging Design:
We are looking for high end tea packaging. We produce high quality teas, and we would like to portray this in our tea packaging. Our teas are made with no artificial flavourings, natural flavourings, or preservatives, so we would also like a natural, organic, high quality look to our tea packaging. Our current logo is a llama. It would be great if you could make the current logo more polished and well made. If you feel that the llama is not well suited or you would like to design the llama differently, we are open to your creative ideas.
General Basic Info:
Keep in mind, we will have both English and French writing on the tea packaging. You do not need to worry about the French writing (we will do the translation), just make sure there is room for it. However, if you feel that you are capable and knowledgeable of incorporating both French and English language into the tea packaging that would be of great help and value.
Back of the Box:
- Will have ingredients and brewing instructions. Basic brewing instructions are: “Add hot water to teabag. Steep for 5-7 minutes, depending on strength preferred. Add milk and your choice of sweetener. Enjoy! See inside panel of box for more detailed instructions”. (The basic brewing instructions, can further be polished or written in a more creative or professional manner).
Front of the Box:
- Will have company name, type of tea, little description of the tea
- 18 teabags
- 54 g (1.9 OZ)
- Should state that this is a product of Alberta, Canada.
Side of the Box:
Any creative wording, slogan, or description about the tea, or whatever you feel would be good on the side of the box.
On the inside flap of the side of the box, there will be detailed instructions on how to brew the tea. These will be different from the simplified brewing instructions on the back of the box. I have attached the advanced brewing instructions as a file. These instructions can further be simplified or reduced to make it easier and cleaner for the consumers to read.
Individual Tea Sachets/ Packets
- These will have a matching look and design of the tea box packaging, except on a smaller scale. Each individual sachet will have the company name, type of tea, little description of the tea in the front of the sachet, while the back will contain the ingredients, and basic brewing instructions.
I have attached a few files, with the dimensions, ingredients, detailed brewing directions, and current logo of the business.
If you have any questions, about the design or packaging please let me know. The winning designer will be required to do a few additional tweaks to finalize the product. Thank you for your time and happy designing!

```html
<!DOCTYPE html>
<html lang="en">
<head>
<meta charset="utf-8">
<title>Velmora Leaf – Velmora Gold Tea Box</title>
<link href="https://fonts.googleapis.com/css2?family=Cinzel:wght@400&family=Pacifico&family=Lobster+Two:ital,wght@0,700;1,700&family=Pathway+Gothic+One&family=Courgette&display=swap" rel="stylesheet">
<style>
  :root {
    --amber: #f7a21b;
    --orange: #e8621c;
    --rust: #b8321a;
    --maroon: #6e1410;
    --band-red: #8e1a12;
    --cocoa: #574741;
    --ink: #2a2220;
    --paper: #ffffff;
    --divider: #d4d4d4;
    --strip: linear-gradient(180deg, var(--amber) 0%, var(--orange) 32%, var(--rust) 62%, var(--maroon) 100%);
  }
  * { box-sizing: border-box; margin: 0; padding: 0; }
  html, body { width: 1200px; height: 1000px; overflow: hidden; background: var(--paper); }
  body { position: relative; font-family: "Pathway Gothic One", sans-serif; color: var(--ink); }

  .view-label { position: absolute; top: 22px; font-family: Arial, sans-serif; font-size: 17px; color: #222; }
  .view-label--front { left: 40px; }
  .view-label--back { left: 652px; }
  .view-divider { position: absolute; left: 592px; top: 0; width: 8px; height: 1000px; background: var(--divider); }

  .panel { position: absolute; top: 110px; height: 840px; background: var(--paper); overflow: hidden; }
  .strip { position: absolute; top: 0; bottom: 0; background: var(--strip); }

  /* Left side panel */
  .side-left { left: 40px; width: 190px; }
  .side-left .strip { right: 0; width: 45px; }
  .side-slogan { position: absolute; left: 8px; top: 68px; width: 140px; font-family: "Courgette", cursive; font-size: 12px; line-height: 1.55; color: var(--band-red); }
  .side-band { position: absolute; left: 0; right: 0; top: 195px; height: 108px; background: var(--cocoa); }
  .side-band p { position: absolute; left: 8px; top: 10px; width: 150px; font-family: "Courgette", cursive; font-size: 12px; line-height: 1.45; color: var(--amber); }
  .side-ribbon { position: absolute; left: 0; right: 0; height: 30px; background: var(--band-red); color: #f3d9cf; font-size: 12px; text-align: center; line-height: 30px; border-top: 1px solid #c0614f; border-bottom: 1px solid #c0614f; padding-right: 45px; white-space: nowrap; }
  .side-ribbon--en { top: 306px; }
  .side-ribbon--fr { top: 340px; }
  .side-copy { position: absolute; left: 8px; width: 138px; font-size: 12.5px; line-height: 1.32; color: var(--ink); }
  .side-copy--en { top: 408px; }
  .side-copy--fr { top: 540px; }

  /* Front panel */
  .front { left: 230px; width: 340px; }
  .front .strip--left { left: 0; width: 40px; }
  .front .strip--right { right: 0; width: 60px; }
  .front-mark { position: absolute; left: 40px; width: 240px; top: 72px; display: flex; align-items: center; justify-content: center; gap: 8px; font-family: "Cinzel", serif; font-size: 15px; color: var(--cocoa); letter-spacing: 1px; }
  .front-mark .dot { width: 14px; height: 14px; border-radius: 50%; background: var(--orange); }
  .brand-band { position: absolute; left: 0; right: 0; top: 195px; height: 155px; background: var(--cocoa); color: var(--paper); text-align: center; padding-left: 30px; }
  .brand-name { font-family: "Cinzel", serif; font-size: 38px; font-weight: 400; margin-top: 35px; letter-spacing: 0.5px; }
  .brand-sub { font-family: "Lobster Two", cursive; font-style: italic; font-weight: 700; font-size: 21px; margin-top: 2px; }
  .tagline-band { position: absolute; left: 0; right: 0; top: 350px; height: 86px; background: var(--band-red); color: var(--paper); padding: 12px 6px 0 24px; }
  .tagline-band .rule { height: 1px; background: #d77a66; margin: 6px 0 6px; }
  .tagline-en { font-size: 12.5px; text-align: center; white-space: nowrap; }
  .tagline-fr { font-family: "Courgette", cursive; font-size: 11px; line-height: 1.45; color: #f6ddd4; }
  .splash { position: absolute; left: 95px; top: 400px; width: 200px; height: 380px; border-radius: 60% 40% 50% 70% / 40% 60% 40% 60%; background: radial-gradient(ellipse at 40% 40%, #f4b043 0%, #d5731f 45%, #8a3612 100%); }
  .variety-badge { position: absolute; left: 25px; top: 440px; width: 150px; height: 150px; border-radius: 50%; background: #e8761c; border: 5px solid #7a1a10; color: var(--paper); text-align: center; padding-top: 18px; }
  .variety-name { font-family: "Pacifico", cursive; font-size: 27px; line-height: 1.05; }
  .variety-count { font-family: "Lobster Two", cursive; font-style: italic; font-size: 15px; border-top: 2px solid var(--paper); width: 100px; margin: 6px auto 0; padding-top: 2px; }
  .front-facts { position: absolute; right: 64px; top: 752px; text-align: right; font-size: 13.5px; line-height: 1.3; color: var(--ink); }
  .front-facts .product-type { font-family: "Lobster Two", cursive; font-style: italic; font-size: 18px; }
  .caffeine-note { position: absolute; left: 70px; top: 810px; font-family: "Lobster Two", cursive; font-style: italic; font-size: 17px; color: var(--maroon); }

  /* Back panel */
  .back { left: 630px; width: 275px; }
  .back .strip { left: 0; width: 62px; }
  .back-content { position: absolute; left: 66px; top: 55px; width: 205px; }
  .back-title { font-family: "Lobster Two", cursive; font-weight: 700; font-size: 17px; color: var(--maroon); }
  .ingredients { font-size: 15.5px; line-height: 1.45; margin-top: 2px; }
  .brew-heading { font-family: "Lobster Two", cursive; font-weight: 700; font-size: 17px; color: var(--maroon); margin: 26px 0 10px 14px; }
  .brew-steps { list-style: none; margin-left: 24px; }
  .brew-steps li { display: flex; align-items: flex-start; gap: 8px; font-size: 12.5px; line-height: 1.3; margin-bottom: 9px; }
  .brew-steps svg { flex: none; width: 22px; height: 22px; }
  .enjoy { font-family: "Lobster Two", cursive; font-weight: 700; font-size: 24px; color: var(--maroon); text-align: center; margin-top: 14px; }
  .enjoy-note { font-size: 10.5px; text-align: center; margin-top: 4px; }
  .back-mark { position: absolute; left: 66px; width: 205px; bottom: 52px; text-align: center; font-family: "Cinzel", serif; color: var(--ink); }
  .back-mark .name { font-size: 13px; }
  .back-mark .dot { display: block; width: 10px; height: 10px; border-radius: 50%; background: var(--orange); margin: 0 auto 3px; }
  .back-mark .sub { font-family: "Lobster Two", cursive; font-style: italic; font-size: 8px; }

  /* Right side panel */
  .side-right { left: 905px; width: 235px; }
  .side-right .strip--left { left: 0; width: 65px; }
  .side-right .strip--right { right: 0; width: 20px; }
  .side-right-band { position: absolute; left: 65px; right: 0; top: 205px; height: 105px; background: var(--cocoa); }
  .side-right-copy { position: absolute; left: 72px; width: 140px; font-size: 12px; line-height: 1.45; color: var(--rust); }
  .side-right-copy--top { top: 90px; }
  .side-right-copy--bottom { top: 615px; color: var(--ink); }
</style>
</head>
<body>
  <div class="view-label view-label--front">Front</div>
  <div class="view-label view-label--back">Back</div>
  <div class="view-divider"></div>

  <section class="panel side-left">
    <div class="strip"></div>
    <p class="side-slogan">Offering authentic, natural Chai Teas and other delicious herbal teas. Teas that enhance your life.</p>
    <div class="side-band">
      <p>Offrant d'authentiques thés Chai naturels et autres délicieuses tisanes. Thés qui améliorent votre vie.</p>
    </div>
    <div class="side-ribbon side-ribbon--en">Crafted for the love of tea</div>
    <div class="side-ribbon side-ribbon--fr">Conçu pour l'amour du thé</div>
    <p class="side-copy side-copy--en">Black tea, warming cardamom and sweet clove meet in every cup. Steeped slowly, this blend brings comfort to your morning and calm to your evening. Made with natural spices and no preservatives, it celebrates the goodness of nature.</p>
    <p class="side-copy side-copy--fr">Le thé noir, la cardamome et le clou de girofle se réunissent dans chaque tasse. Infusé lentement, ce mélange réconforte vos matins et apaise vos soirées. Fait d'épices naturelles, sans agents de conservation, il célèbre la bonté de la nature.</p>
  </section>

  <section class="panel front">
    <div class="strip strip--left"></div>
    <div class="strip strip--right"></div>
    <div class="front-mark"><span class="dot"></span>Velmora Leaf</div>
    <div class="brand-band">
      <h1 class="brand-name">VELMORA LEAF</h1>
      <p class="brand-sub">The Tea Company + More</p>
    </div>
    <div class="splash" role="img" aria-label="Splash of poured amber chai tea"></div>
    <div class="tagline-band">
      <p class="tagline-en">An exotic blend of black tea, cardamom, fennel, cloves, Cinnamon, &amp; ginger.</p>
      <div class="rule"></div>
      <p class="tagline-fr">Un mélange exotique de thé noir, de cardamome, le fenouil, clous de girofle, la cannelle et le gingembre.</p>
    </div>
    <div class="variety-badge">
      <div class="variety-name">Velmora<br>Gold</div>
      <div class="variety-count">18 teabags</div>
    </div>
    <div class="front-facts">
      <div class="product-type">Chai Tea</div>
      <div>54 g (1.9 OZ)</div>
      <div>A Product Of Alberta, Canada.</div>
    </div>
    <div class="caffeine-note">Caffeine</div>
  </section>

  <section class="panel back">
    <div class="strip"></div>
    <div class="back-content">
      <h2 class="back-title">Velmora Gold Ingredients</h2>
      <p class="ingredients">Black tea, cardamom, cloves, fennel, ginger, and cinnamon</p>

      <h3 class="brew-heading">Quick Brewing</h3>
      <ul class="brew-steps">
        <li><svg viewBox="0 0 24 24" fill="none" stroke="#2a2220" stroke-width="1.8"><path d="M4 11h12v6a4 4 0 0 1-4 4H8a4 4 0 0 1-4-4z"/><path d="M16 13h2a2 2 0 0 1 0 4h-2"/><path d="M8 3v5M12 4v4"/></svg>Add hot water to teabag.</li>
        <li><svg viewBox="0 0 24 24" fill="none" stroke="#2a2220" stroke-width="1.8"><path d="M4 13h12v4a4 4 0 0 1-4 4H8a4 4 0 0 1-4-4z"/><circle cx="14" cy="6" r="4"/><path d="M14 4v2h2"/></svg>Steep for 5-7 minutes, depending on strength preferred</li>
        <li><svg viewBox="0 0 24 24" fill="none" stroke="#2a2220" stroke-width="1.8"><path d="M3 13h11v4a4 4 0 0 1-4 4H7a4 4 0 0 1-4-4z"/><rect x="15" y="5" width="6" height="12"/><path d="M15 9h6"/></svg>Add milk and your choice of sweetener.</li>
      </ul>
      <p class="enjoy">Enjoy!</p>
      <p class="enjoy-note">See inside panel of box for more detailed instructions</p>

      <h3 class="brew-heading">Brewing rapide</h3>
      <ul class="brew-steps">
        <li><svg viewBox="0 0 24 24" fill="none" stroke="#2a2220" stroke-width="1.8"><path d="M4 11h12v6a4 4 0 0 1-4 4H8a4 4 0 0 1-4-4z"/><path d="M16 13h2a2 2 0 0 1 0 4h-2"/><path d="M8 3v5M12 4v4"/></svg>Ajouter de l'eau chaude pour sachet de thé.</li>
        <li><svg viewBox="0 0 24 24" fill="none" stroke="#2a2220" stroke-width="1.8"><path d="M4 13h12v4a4 4 0 0 1-4 4H8a4 4 0 0 1-4-4z"/><circle cx="14" cy="6" r="4"/><path d="M14 4v2h2"/></svg>Laisser macérer pendant 5-7 minutes, selon la force préféré</li>
        <li><svg viewBox="0 0 24 24" fill="none" stroke="#2a2220" stroke-width="1.8"><path d="M3 13h11v4a4 4 0 0 1-4 4H7a4 4 0 0 1-4-4z"/><rect x="15" y="5" width="6" height="12"/><path d="M15 9h6"/></svg>Ajouter le lait et votre choix d'édulcorant.</li>
      </ul>
      <p class="enjoy">Profitez!</p>
      <p class="enjoy-note">Voir panneau intérieur de la boîte pour des instructions plus détaillées.</p>
    </div>
    <div class="back-mark">
      <span class="dot"></span>
      <div class="name">VELMORA LEAF</div>
      <div class="sub">The Tea Company + More</div>
    </div>
  </section>

  <section class="panel side-right">
    <div class="strip strip--left"></div>
    <div class="strip strip--right"></div>
    <p class="side-right-copy side-right-copy--top">Lorem ipsum dolor sit amet, consectetuer adipiscing elit. Aenean commodo ligula eget dolor. Aenean massa. Cum sociis natoque penatibus et magnis dis parturient montes, nascetur ridiculus mus.</p>
    <div class="side-right-band"></div>
    <p class="side-right-copy side-right-copy--bottom">Donec quam felis, ultricies nec, pellentesque eu, pretium quis, sem. Nulla consequat massa quis enim. Donec pede justo, fringilla vel, aliquet nec, vulputate eget, arcu. In enim justo, rhoncus ut, imperdiet a, venenatis vitae, justo. Nullam dictum felis eu pede mollis pretium. Integer tincidunt. Cras dapibus.</p>
  </section>
</body>
</html>
```